A corporate Christmas card for Crestmoor University

We need a Christmas card design for a University. We are a private university with a reputation for academic excellence. We also have a strong christian identity. The final design must communicate elegance, grace and our Christian background.

Target Market(s)

managers and company executives; people with at least a college degree; thirty to 50 years old

Industry/Entity Type

University

Colors

Designer to choose colors to be used in the design.

Requirements
Must have
• The card must have 4 pages and use only the photos attached.
Size of card when folded: 5" x 7"
An image of the nativity
The University's name and logo
The University's URL (www.cmu-lakeview.edu.ng)
The expression 'Merry Christmas'
One of the inner pages must have the following discreetly placed:
"‘Look, the virgin shall conceive and bear a son, and they shall name him Emmanuel’, which means, ‘God is with us.’

Matthew chapter 1, vs 23"
Nice to have
• The University's name and logo and the University's URL (www.cmu-lakeview.edu.ng) should be on the back page.
Should not have
• The expression 'seasons greetings' or 'happy holidays'

```html
<!DOCTYPE html>
<html lang="en">
<head>
<meta charset="utf-8">
<title>Crestmoor University — Christmas Card, Scripture Page</title>
<link rel="stylesheet" href="https://fonts.googleapis.com/css2?family=Sorts+Mill+Goudy:ital@1&family=Arimo:wght@400;700&display=swap">
<style>
  :root {
    --page: #ffffff;
    --frame: #1f2fd0;
    --ink: #111111;
    --gold: #d9b23c;
    --gold-soft: #f0d27a;
    --brand: #2237b4;
    --link: #3a57d6;
  }
  html, body {
    margin: 0;
    padding: 0;
    width: 857px;
    height: 1200px;
    overflow: hidden;
    background: var(--page);
  }
  .card {
    position: relative;
    width: 857px;
    height: 1200px;
    box-sizing: border-box;
    border: 3px solid var(--frame);
    background: var(--page);
  }
  .scripture {
    position: absolute;
    left: 0;
    right: 0;
    top: 282px;
    margin: 0;
    text-align: center;
    font-family: "Sorts Mill Goudy", "Goudy Old Style", Georgia, serif;
    font-style: italic;
    font-size: 34px;
    color: var(--ink);
    -webkit-text-stroke: 0.5px var(--ink);
  }
  .scripture__line {
    display: block;
    line-height: 75px;
  }
  .scripture__source {
    position: absolute;
    left: 416px;
    top: 594px;
    font-family: "Sorts Mill Goudy", "Goudy Old Style", Georgia, serif;
    font-style: italic;
    font-size: 27px;
    line-height: 34px;
    color: var(--ink);
    -webkit-text-stroke: 0.4px var(--ink);
  }
  .flourish {
    position: absolute;
    border-radius: 8px;
    background: linear-gradient(135deg, var(--gold-soft), var(--gold));
    opacity: 0.85;
  }
  .flourish--top-right { left: 636px; top: 250px; width: 120px; height: 112px; }
  .flourish--bottom-left { left: 106px; top: 576px; width: 142px; height: 96px; }
  .signature {
    position: absolute;
    left: 260px;
    top: 972px;
    width: 460px;
    height: 130px;
  }
  .signature__mark {
    position: absolute;
    left: 8px;
    top: 8px;
  }
  .signature__name {
    position: absolute;
    left: 134px;
    top: 14px;
    margin: 0;
    font-family: "Arimo", Arial, sans-serif;
    font-weight: 700;
    font-size: 30px;
    line-height: 32px;
    color: var(--brand);
    text-transform: uppercase;
  }
  .signature__url {
    position: absolute;
    left: 134px;
    top: 94px;
    font-family: "Arimo", Arial, sans-serif;
    font-weight: 400;
    font-size: 23px;
    color: var(--link);
  }
</style>
</head>
<body>
  <main class="card">
    <div class="flourish flourish--top-right" role="img" aria-label="Gold baroque corner ornament"></div>

    <p class="scripture">
      <span class="scripture__line">“‘Look, the virgin</span>
      <span class="scripture__line">shall conceive and bear a son,</span>
      <span class="scripture__line">and they shall name him Emmanuel’,</span>
      <span class="scripture__line">which means, ‘God is with us.’</span>
    </p>

    <div class="flourish flourish--bottom-left" role="img" aria-label="Gold baroque corner ornament"></div>
    <span class="scripture__source">Matthew chapter 1, vs 23”</span>

    <footer class="signature">
      <svg class="signature__mark" width="104" height="104" viewBox="0 0 104 104" aria-hidden="true">
        <circle cx="52" cy="52" r="50" fill="var(--brand)"/>
      </svg>
      <p class="signature__name">Crestmoor<br>University</p>
      <span class="signature__url">www.cmu-lakeview.edu.ng</span>
    </footer>
  </main>
</body>
</html>
```